ultra-minimalist business card

front (black background, matte):

tarik b. hosseny
writer | photographer
get@tarikhosseny.com

back (white background, matte):

a picture speaks a thousand words;
a word draws a thousand pictures.

www.tarikhosseny.com

all text should be small (white or silver - as long as it shows against the black - on the front; black or gray - as long as it shows against the white - on the back).

feel free to get creative in terms of arrangement, alignment, and font type, but remember, the overall style is minimalist, so nothing too fancy, please.

thanks.

```html
<!DOCTYPE html>
<html lang="en">
<head>
<meta charset="utf-8">
<title>tarik b. hosseny — business card</title>
<link rel="stylesheet" href="https://fonts.googleapis.com/css2?family=EB+Garamond:wght@400&display=swap">
<style>
  :root {
    --stage: #1c1c1c;
    --card-front: #141414;
    --card-back: #ffffff;
    --ink-light: #e6e6e6;
    --ink-muted: #b4b4b4;
    --ink-dark: #1a1a1a;
    --font-serif: "EB Garamond", Georgia, serif;
  }
  * { box-sizing: border-box; margin: 0; padding: 0; }
  html, body {
    width: 1200px;
    height: 692px;
    overflow: hidden;
    background: var(--stage);
    font-family: var(--font-serif);
  }
  .card-stage {
    position: relative;
    width: 1200px;
    height: 692px;
  }
  .card {
    position: absolute;
    top: 203px;
    width: 500px;
    height: 286px;
    border-radius: 3px;
  }
  .card--front {
    left: 67px;
    background: var(--card-front);
    color: var(--ink-light);
    box-shadow: 0 0 0 1px #2a2a2a;
  }
  .card--back {
    left: 633px;
    background: var(--card-back);
    color: var(--ink-dark);
  }
  .card__name {
    position: absolute;
    top: 42px;
    left: 44px;
    font-size: 27px;
    font-weight: 400;
    letter-spacing: 0.02em;
    line-height: 1;
  }
  .card__role {
    position: absolute;
    top: 78px;
    left: 45px;
    font-size: 15px;
    color: var(--ink-muted);
    letter-spacing: 0.03em;
  }
  .card__email {
    position: absolute;
    right: 36px;
    bottom: 30px;
    font-size: 12px;
    color: var(--ink-muted);
    letter-spacing: 0.03em;
  }
  .card__quote {
    position: absolute;
    top: 40px;
    left: 44px;
    font-size: 15px;
    line-height: 1.15;
    letter-spacing: 0.01em;
  }
  .card__quote span { display: block; }
  .card__web {
    position: absolute;
    right: 40px;
    bottom: 32px;
    font-size: 13px;
    letter-spacing: 0.03em;
  }
</style>
</head>
<body>
  <main class="card-stage">
    <section class="card card--front" aria-label="Card front">
      <h1 class="card__name">tarik b. hosseny</h1>
      <p class="card__role">writer | photographer</p>
      <p class="card__email">get@tarikhosseny.com</p>
    </section>
    <section class="card card--back" aria-label="Card back">
      <p class="card__quote">
        <span>A picture speaks a thousand words;</span>
        <span>A word draws a thousand pictures.</span>
      </p>
      <p class="card__web">www.tarikhosseny.com</p>
    </section>
  </main>
</body>
</html>
```